Flicktor - photography in NYC - leveraging big data and robotics

We've got a photography business in NYC. It is kind of on-demand photographers, but actually is just five of us who work as a team. Over the last three years we've taken tens of thousands of photographs and are now sitting on a load of great work. We want to leverage that in a way that lets people book either by event type or location. So, they would click on Harrow Green and a load of examples of our work would pop up. Or Wedding Shower, and relevant examples would pop up. We've got the pictures structured pretty well to enable this. Now we just need a website that illustrates this and then leads through the booking process (time, location, date, contact etc.) and payment.

Target Market(s)

Everyone - corporates, real estate, tourists, families, headshots, bloggers, products, wedding showers, baby showers, engagements, venues, restaurants/bars, holiday pictures, Marlow Hall weddings, kids birthday parties, adult birthday parties, PR companies, corporate events.... long list.

Industry/Entity Type

Photographer

Number of Pages Required

5+ page

Colors

Designer to choose colors to be used in the design.

Requirements
Must have
• A great, engaging landing page which people can choose by event type or location. This would then pull in examples of our work in that location or in that event type. Then they go through the booking process. This is simple capturing key details - see here https://flicktorphoto.example/book/
Nice to have
• Social links
Should not have
• Nothing specific.

```html
<!DOCTYPE html>
<html lang="en">
<head>
<meta charset="utf-8">
<title>Flicktor – Photography in NYC</title>
<link rel="stylesheet" href="https://fonts.googleapis.com/css2?family=Alegreya:ital,wght@0,400;0,700;1,400&family=Roboto:wght@400;700&display=swap">
<style>
  :root{
    --canvas:#e2e2e2;
    --charcoal:#454545;
    --olive:#7d6e0a;
    --olive-deep:#4d4205;
    --green:#5a8a34;
    --green-light:#bde0a0;
    --indigo:#2e2f8f;
    --orange:#f39a1e;
    --white:#ffffff;
    --ink:#222222;
    --muted:#d9d9d9;
    --chip:#eef3ea;
  }
  *{box-sizing:border-box;margin:0;padding:0}
  html,body{width:1200px;height:1200px;overflow:hidden;background:var(--canvas)}
  body{display:flex;align-items:center;justify-content:center;font-family:"Alegreya",serif;color:var(--white)}
  a{color:inherit;text-decoration:none}
  .page{width:280px;height:1190px;display:flex;flex-direction:column;box-shadow:0 2px 10px rgba(0,0,0,.15)}
  section,header,footer{position:relative;flex:none}

  .site-nav{height:23px;background:var(--charcoal);display:flex;align-items:center;padding:0 20px;justify-content:space-between}
  .site-nav .brand{font-size:9px;letter-spacing:.5px}
  .site-nav ul{display:flex;gap:14px;list-style:none;font-size:5.5px}

  .hero{height:150px;overflow:hidden}
  .hero .photo{position:absolute;inset:0;background:linear-gradient(180deg,var(--olive) 0%,#6a5c08 60%,var(--olive-deep) 100%)}
  .hero .rocks{position:absolute;left:0;right:0;bottom:0;height:45px;background:linear-gradient(180deg,#3a2d08,#241b05)}
  .hero h1{position:absolute;left:20px;top:44px;font-style:italic;font-weight:400;font-size:15.5px;letter-spacing:.3px}
  .btn{display:inline-block;background:var(--indigo);border-radius:8px;font-size:6px;padding:2px 17px;line-height:1.3}
  .hero .btn{position:absolute;left:20px;top:76px}

  .create{height:114px;background:var(--charcoal);text-align:center;padding-top:9px}
  .section-title{font-size:8px;font-weight:700}
  .create .section-title span{color:#c9a66b;font-weight:400}
  .blurb{font-family:"Roboto",sans-serif;font-size:4px;line-height:1.4;color:var(--muted);margin:5px auto 0;width:170px}
  .features{display:flex;justify-content:space-between;padding:0 14px;margin-top:12px}
  .feature{width:72px}
  .feature .icon{width:11px;height:11px;border:1px solid #ccc;border-radius:50%;margin:0 auto 3px}
  .feature.active .icon{border-color:#5b7ee8;border-width:1.5px}
  .feature h3{font-size:5px;font-weight:400}
  .feature p{font-family:"Roboto",sans-serif;font-size:3px;color:#aaa;margin-top:2px;line-height:1.4}

  .services{height:261px;background:var(--green);padding:14px 20px 0}
  .services > .section-title{text-align:center}
  .services > .blurb{margin-top:1px;width:200px;text-align:center}
  .service{display:flex;justify-content:space-between;align-items:center;margin-top:12px}
  .service .text{width:145px}
  .service.reverse{flex-direction:row-reverse}
  .service.reverse .text{text-align:right}
  .service h3{font-size:5.5px;font-weight:400}
  .service p{font-family:"Roboto",sans-serif;font-size:3.6px;line-height:1.45;color:#eee;margin-top:5px}
  .service .thumb{width:77px;height:50px;border:1px dashed var(--green-light)}
  .thumb.house{background:linear-gradient(160deg,#2f4d8a,#5a76b4 60%,#c9c1a3)}
  .thumb.wedding{background:linear-gradient(180deg,#2d3b2a,#6f7d6a 55%,#c9b9b3)}
  .thumb.tourists{background:linear-gradient(180deg,#8fa9c8,#6a6f7d 60%,#4a4a52)}

  .portfolio{height:232px;background:var(--white);color:var(--ink);padding-top:18px;text-align:center}
  .gallery{display:grid;grid-template-columns:repeat(3,77px);grid-auto-rows:57px;gap:3px;justify-content:center;margin-top:18px}
  .tile{position:relative;text-align:left}
  .tile span{position:absolute;left:4px;bottom:8px;font-size:4.5px;color:var(--white);font-weight:700}
  .t1{background:linear-gradient(135deg,#1e2a38,#5b6470)}
  .t2{background:linear-gradient(180deg,#4a7fb5,#b9c7d3 70%,#7c7466)}
  .t3{background:linear-gradient(180deg,#3d4c5c,#6b7a52)}
  .t4{background:linear-gradient(135deg,#9aa3ad,#2c2f34)}
  .t5{background:linear-gradient(180deg,#5f7a8c,#2f3f44)}
  .t6{background:linear-gradient(180deg,#1f2633,#7a2a36)}
  .browse{width:237px;margin:10px auto 0;text-align:left;font-family:"Roboto",sans-serif}
  .browse-row{display:flex;align-items:center;gap:3px;margin-top:4px;flex-wrap:nowrap}
  .browse-row b{font-family:"Alegreya",serif;font-size:5px;width:38px;flex:none}
  .chip{font-size:3.8px;line-height:1;padding:2px 5px;border-radius:6px;background:var(--chip);color:var(--ink);white-space:nowrap}
  .chip.on{background:var(--green);color:var(--white)}

  .stats{height:130px;background:linear-gradient(160deg,#2c2c2c,#4a4a4a 55%,#262626);padding:0 20px}
  .counters{display:flex;justify-content:space-between;padding-top:24px}
  .counter{text-align:center;font-family:"Roboto",sans-serif}
  .counter b{display:block;font-size:8px;font-weight:400}
  .counter small{font-size:3.5px;color:#ccc}
  .steps{display:flex;justify-content:space-between;list-style:none;margin-top:12px;font-family:"Roboto",sans-serif}
  .steps li{display:flex;flex-direction:column;align-items:center;gap:2px;font-size:3.6px;color:#ddd;width:40px}
  .steps i{font-style:normal;width:8px;height:8px;border-radius:50%;border:1px solid var(--orange);color:var(--orange);font-size:4px;display:flex;align-items:center;justify-content:center}
  .cta{position:absolute;left:0;right:0;bottom:0;height:36px;background:rgba(70,60,40,.55);display:flex;align-items:center;justify-content:space-between;padding:0 32px 0 21px}
  .cta p{font-size:6px}
  .cta .btn{background:var(--orange);font-size:4.5px;padding:1.5px 12px}

  .testimonial{height:135px;background:var(--green);text-align:center;padding-top:15px}
  .avatars{display:flex;align-items:center;justify-content:center;gap:22px;margin-top:15px}
  .avatar{width:12px;height:12px;border-radius:50%;background:linear-gradient(#c08a6a,#4a2f22)}
  .avatar.main{width:21px;height:21px;border:1.5px solid var(--white)}
  .chev{font-size:9px;color:#a8cf8a}
  .quote-name{font-size:4px;color:var(--orange);margin-top:2px}
  .quote-role{font-size:3px;color:#ddd}
  .testimonial .blurb{font-size:3.3px;width:130px;margin-top:4px}

  .site-footer{height:145px;background:var(--charcoal);padding:24px 20px 0;font-size:5px}
  .cols{display:flex;justify-content:space-between}
  .cols h4{font-weight:400;font-size:5.5px;margin-bottom:6px}
  .cols p,.cols li{font-family:"Roboto",sans-serif;font-size:3.5px;line-height:1.5;color:#ddd;list-style:none}
  .about{width:75px}
  .follow{margin-top:6px}
  .contact li{display:flex;align-items:center;gap:4px}
  .contact li.indent{padding-left:9px}
  .dot-row{display:flex;gap:3px;margin-top:3px}
  .dot{width:6px;height:6px;border-radius:50%;background:var(--white)}
  .bottom{position:absolute;left:20px;right:20px;bottom:10px;display:flex;justify-content:space-between;align-items:center}
  .bottom .brand{font-size:8px}
  .bottom small{font-family:"Roboto",sans-serif;font-size:3.5px;font-weight:700}
  .to-top{position:absolute;right:14px;bottom:24px}
</style>
</head>
<body>
<main class="page">
  <header class="site-nav">
    <span class="brand">LOGO</span>
    <ul><li>Home</li><li>Portfolio</li><li>Service</li><li>Blog</li><li>Contact</li></ul>
  </header>

  <section class="hero">
    <div class="photo" role="img" aria-label="Photographer with a tripod silhouetted on rocks against an amber sky"></div>
    <div class="rocks"></div>
    <h1>Welcome to Flicktor</h1>
    <a class="btn" href="#portfolio">View More</a>
  </section>

  <section class="create">
    <h2 class="section-title">What we <span>Create</span></h2>
    <p class="blurb">Five photographers working as one team across the city, ready for any event, venue or moment you want captured.</p>
    <div class="features">
      <div class="feature"><div class="icon"></div><h3>Urban Exploration</h3><p>Streets, rooftops and parks shot with a local eye.</p></div>
      <div class="feature active"><div class="icon"></div><h3>Shoot Amazing Film</h3><p>Short films for events, brands and families.</p></div>
      <div class="feature"><div class="icon"></div><h3>Best Photographer</h3><p>Thousands of sessions over three busy years.</p></div>
    </div>
  </section>

  <section class="services">
    <h2 class="section-title">Services</h2>
    <p class="blurb">Book by event type or location and see our work first.</p>
    <div class="service">
      <div class="text"><h3>Property Photography</h3><p>Bright, honest images of homes and venues for listings, agents and owners who want every room to look its best on screen.</p></div>
      <div class="thumb house" role="img" aria-label="Blue house lit at dusk"></div>
    </div>
    <div class="service reverse">
      <div class="text"><h3>Wedding Photography</h3><p>Showers, engagements and Marlow Hall weddings, covered from first look to last dance by a calm and friendly team.</p></div>
      <div class="thumb wedding" role="img" aria-label="Outdoor wedding aisle with flowers"></div>
    </div>
    <div class="service">
      <div class="text"><h3>Tourist Photography</h3><p>Holiday portraits at Harrow Green and city landmarks, so visitors go home with real pictures of their trip.</p></div>
      <div class="thumb tourists" role="img" aria-label="Group of travellers posing outdoors"></div>
    </div>
  </section>

  <section class="portfolio" id="portfolio">
    <h2 class="section-title">Portfolio</h2>
    <div class="gallery">
      <div class="tile t1" role="img" aria-label="Camera held in hand"><span>Photography</span></div>
      <div class="tile t2" role="img" aria-label="Person photographing from a rocky summit"></div>
      <div class="tile t3" role="img" aria-label="Mountain landscape video still"><span>Landscape</span></div>
      <div class="tile t4" role="img" aria-label="Camera on a tripod close-up"></div>
      <div class="tile t5" role="img" aria-label="Hiker by a mountain lake"></div>
      <div class="tile t6" role="img" aria-label="City street with red lights at night"></div>
    </div>
    <nav class="browse" aria-label="Browse our work">
      <div class="browse-row"><b>By event</b><span class="chip on">Wedding Shower</span><span class="chip">Corporate</span><span class="chip">Family</span><span class="chip">Headshots</span><span class="chip">Birthday</span></div>
      <div class="browse-row"><b>By location</b><span class="chip on">Harrow Green</span><span class="chip">Marlow Hall</span><span class="chip">Riverside</span><span class="chip">Midtown</span></div>
    </nav>
  </section>

  <section class="stats" role="img" aria-label="Dark camera gear backdrop">
    <div class="counters">
      <div class="counter"><b>30+</b><small>Year Experience</small></div>
      <div class="counter"><b>115+</b><small>Happy Client</small></div>
      <div class="counter"><b>90+</b><small>Complete Project</small></div>
      <div class="counter"><b>10+</b><small>Award Won</small></div>
    </div>
    <ol class="steps" aria-label="Booking steps">
      <li><i>1</i>Event</li>
      <li><i>2</i>Location</li>
      <li><i>3</i>Date &amp; Time</li>
      <li><i>4</i>Contact</li>
      <li><i>5</i>Payment</li>
    </ol>
    <div class="cta"><p>Looking for Best Photographer?</p><a class="btn" href="https://flicktorphoto.example/book/">Click here</a></div>
  </section>

  <section class="testimonial">
    <h2 class="section-title">Testimonial</h2>
    <div class="avatars">
      <span class="chev">‹</span>
      <div class="avatar" role="img" aria-label="Client portrait"></div>
      <div class="avatar" role="img" aria-label="Client portrait"></div>
      <div class="avatar main" role="img" aria-label="Featured client portrait"></div>
      <div class="avatar" role="img" aria-label="Client portrait"></div>
      <div class="avatar" role="img" aria-label="Client portrait"></div>
      <span class="chev">›</span>
    </div>
    <p class="quote-name">Ana Rivers</p>
    <p class="quote-role">Regular Client</p>
    <p class="blurb">“They found the perfect spot, kept the kids laughing and sent the photos within days. We book them every year.”</p>
  </section>

  <footer class="site-footer">
    <div class="cols">
      <div class="about"><h4>About me.</h4><p>“Five photographers, one team, shooting every corner of the city since day one.”</p></div>
      <div>
        <h4>Legal</h4>
        <ul><li>Privacy policy</li><li>Cookie policy</li><li>Terms and Condition</li></ul>
        <h4 class="follow">Follow us</h4>
        <div class="dot-row"><span class="dot"></span><span class="dot"></span><span class="dot"></span></div>
      </div>
      <div class="contact">
        <h4>Contact us.</h4>
        <ul>
          <li><svg width="5" height="5" viewBox="0 0 10 10"><rect x="2" y="0.5" width="6" height="9" rx="1" fill="none" stroke="#fff"/></svg>012-555-0146</li>
          <li class="indent">012-555-0147</li>
          <li><svg width="5" height="5" viewBox="0 0 10 10"><rect x="0.5" y="2" width="9" height="6" fill="none" stroke="#fff"/><path d="M0.5 2 5 5.5 9.5 2" fill="none" stroke="#fff"/></svg>hello@flicktorphoto.example</li>
        </ul>
      </div>
    </div>
    <svg class="to-top" width="6" height="4" viewBox="0 0 6 4"><path d="M0.5 3.5 3 1 5.5 3.5" fill="none" stroke="#f39a1e"/></svg>
    <div class="bottom"><span class="brand">LOGO</span><small>Copyright © 2018. All rights reserved.</small></div>
  </footer>
</main>
</body>
</html>
```